quillora.link quillora.space quillora.press website

The website is named QUILLORA and it will have 3 domain names. quillora.link, press, space.
I'd like it to be viewed on Pads, pcs and phones.

page menu:

quillora.link(start page): presentation of company. (creative, design, app, new product innovation.)
Here we'll need sosial media icons: twitter, instagram, facebook, linkedin. (light but some 'fruity' colors)

quillora.press: blog. It will be a 75% picture blog > rest will be text. I need to be able to resize pictures and shape columns to picture size. (light but some 'fruity' colors)

quillora.space : the fun part of this web design, however, on entering the page I'd like a non-disclosure agreement where viewer simply click "yes, I agree" after filling out contact info. (check attached document)
We will have space here for uploading PDF files viewers can download. There is also a blog space here to tell in brief about the PDF file. (maybe a space/sci-fi theme her e.g spacechimp, Laika the space dog?)

I will attach the logo here I want you to use > and develop for the .space .press webpage. The logo i uploaded is for the .link page.

Target Market(s)

venture capitalists

Number of Pages Required

3 page

Requirements
Must have
• a few 'fruity colors' but mostly white and grey

```html
<!DOCTYPE html>
<html lang="en">
<head>
<meta charset="utf-8">
<title>Quillora</title>
<link rel="stylesheet" href="https://fonts.googleapis.com/css2?family=Lato:wght@400;700;900&family=Oswald:wght@600&display=swap">
<style>
:root{
  --dark:#3a3a3a;
  --black:#111;
  --white:#fff;
  --band:#ededed;
  --text:#333;
  --green:#5aa64b;
  --green-deep:#2f6e35;
  --red:#d9463a;
  --ring:#8e8f94;
  --social-1:#2f7fd8;
  --social-2:#45a8e6;
  --social-3:#6b4f3f;
  --social-4:#1a86c8;
}
*{margin:0;padding:0;box-sizing:border-box}
html,body{width:1200px;height:1148px;overflow:hidden;background:var(--white)}
body{font-family:'Lato',sans-serif;color:var(--text);position:relative}
.abs{position:absolute}
.topbar{left:0;top:0;width:1200px;height:65px;background:var(--dark)}
.contact-top{top:12px;display:flex;align-items:center;gap:9px;color:var(--white);font-size:16px;white-space:nowrap}
.ring-icon{width:38px;height:38px;flex:none;border:2px solid #cfcfcf;border-radius:50%;display:flex;align-items:center;justify-content:center}
.navband{left:0;top:65px;width:1200px;height:51px;background:var(--white);border-top:1px dashed #999;border-bottom:1px dashed var(--red)}
.mainnav{left:328px;top:80px;display:flex;font-weight:700;font-size:16px}
.mainnav a{color:#222;text-decoration:none}
.mainnav .active{color:var(--green)}
.mainnav .sep{color:#ccc;margin:0 20px;font-weight:400}
.social-top{left:982px;top:76px;display:flex;gap:5px}
.social-top span{width:30px;height:30px;border-radius:6px;border:2px solid #cfe4f5}
.brand{left:80px;top:12px;width:213px;height:133px;background:var(--white);box-shadow:0 6px 8px rgba(0,0,0,.35);padding:7px;z-index:5}
.brand div{width:100%;height:100%;border:1px solid var(--red);border-radius:4px;display:flex;align-items:center;justify-content:center;font-weight:900;font-size:30px;color:#222;letter-spacing:1px}
.hero{left:0;top:116px;width:1200px;height:506px;background:linear-gradient(90deg,#1a2236 0%,#23345a 50%,#3c5a8e 75%,#2b3f66 100%)}
.hero h1{position:absolute;left:80px;top:236px;font-family:'Oswald',sans-serif;font-weight:600;font-size:32px;line-height:41px;color:var(--white);letter-spacing:.5px}
.features{left:0;top:622px;width:1200px;height:129px;background:var(--band);border-bottom:1px solid #ddd;z-index:2}
.outer{width:160px;height:160px;border-radius:50%;background:var(--ring);top:535px;z-index:1}
.inner{width:134px;height:134px;border-radius:50%;background:#f1f1f1;top:548px;z-index:3;display:flex;align-items:center;justify-content:center}
.feat-label{top:698px;width:200px;text-align:center;font-weight:700;font-size:17px;color:#222;z-index:3;line-height:20px}
.about{left:0;top:751px;width:1200px;height:231px;background:var(--band);text-align:center}
.about h2{margin-top:45px;font-size:32px;font-weight:700;color:#222}
.about h2 em{font-style:normal;color:var(--green-deep)}
.about p{width:980px;margin:18px auto 0;font-size:13.6px;line-height:25.5px;color:#333}
.footnav{left:0;top:982px;width:1200px;height:64px;background:var(--green);display:flex;justify-content:center;align-items:center;font-size:15px}
.footnav a{color:var(--white);text-decoration:none}
.footnav a.active{color:#1e3a1c}
.footnav .star{color:#1e3a1c;margin:0 24px;font-size:12px}
.contactbar{left:0;top:1046px;width:1200px;height:58px;background:var(--dark);color:#ddd;font-size:14.5px}
.contactbar .item{position:absolute;top:0;height:58px;display:flex;align-items:center;gap:8px;white-space:nowrap}
.email-in{left:885px;top:14px;width:200px;height:32px;background:#2e2e2e;color:#ccc;font-size:12.5px;padding:8px 10px}
.go{left:1085px;top:14px;width:35px;height:32px;background:#e04a2a;color:var(--white);font-weight:700;font-size:15px;display:flex;align-items:center;justify-content:center}
.bottom{left:0;top:1104px;width:1200px;height:44px;background:var(--black);color:#ddd;font-size:13.5px}
.bottom .copy{position:absolute;left:80px;top:13px}
.social-foot{position:absolute;left:985px;top:8px;display:flex;gap:10px}
.social-foot span{width:30px;height:30px;border-radius:50%;background:var(--white)}
</style>
</head>
<body>
<div class="abs topbar"></div>
<div class="abs contact-top" style="left:732px">
  <div class="ring-icon"><svg width="16" height="12" viewBox="0 0 16 12"><rect x="1" y="1" width="14" height="10" rx="1.5" fill="none" stroke="#fff" stroke-width="1.5"/><path d="M1 2l7 5 7-5" fill="none" stroke="#fff" stroke-width="1.5"/></svg></div>
  <span>info@quillora.com</span>
</div>
<div class="abs contact-top" style="left:938px">
  <div class="ring-icon"><svg width="16" height="16" viewBox="0 0 16 16"><path d="M3 1l3 3-2 2c1 2 3 4 5 5l2-2 3 3-2 2C7 14 2 9 1 3z" fill="#fff"/></svg></div>
  <span>+1 555 0134 207</span>
</div>

<div class="abs navband"></div>
<nav class="abs mainnav">
  <a class="active" href="#">HOME</a><span class="sep">/</span>
  <a href="#">ABOUT</a><span class="sep">/</span>
  <a href="#">SERVICES</a><span class="sep">/</span>
  <a href="#">BLOG</a>
</nav>
<div class="abs social-top" aria-label="Social links">
  <span style="background:var(--social-1)"></span>
  <span style="background:var(--social-2)"></span>
  <span style="background:var(--social-3)"></span>
  <span style="background:var(--social-4)"></span>
</div>

<div class="abs brand"><div>QUILLORA</div></div>

<section class="abs hero" role="img" aria-label="Businessperson drawing a cloud network diagram linking monitor, phone, tablet, laptop and servers">
  <h1>We Made Creative Design &amp; Application<br>For New Product Innovation</h1>
</section>

<div class="abs features"></div>

<div class="abs outer" style="left:124px"></div>
<div class="abs inner" style="left:137px">
  <svg width="76" height="70" viewBox="0 0 76 70"><rect x="2" y="14" width="72" height="44" rx="3" fill="#555"/><rect x="8" y="20" width="60" height="32" fill="#f1f1f1"/><rect x="30" y="58" width="16" height="6" fill="#555"/><rect x="22" y="64" width="32" height="4" rx="2" fill="#555"/><path d="M52 2l6 5-20 26-8 3 2-8z" fill="#555"/></svg>
</div>
<div class="abs feat-label" style="left:104px">CREATIVE</div>

<div class="abs outer" style="left:390px"></div>
<div class="abs inner" style="left:403px">
  <svg width="72" height="72" viewBox="0 0 72 72"><g fill="none" stroke="#555" stroke-width="4"><rect x="4" y="29" width="64" height="14" transform="rotate(-45 36 36)"/><rect x="4" y="30" width="58" height="12" transform="rotate(45 36 36)"/></g><path d="M60 58l6 10-10-4z" fill="#555"/></svg>
</div>
<div class="abs feat-label" style="left:370px">DESIGN</div>

<div class="abs outer" style="left:657px"></div>
<div class="abs inner" style="left:670px">
  <svg width="60" height="72" viewBox="0 0 60 72"><rect x="4" y="2" width="30" height="66" rx="4" fill="#555"/><rect x="8" y="10" width="22" height="46" fill="#f1f1f1"/><circle cx="19" cy="62" r="3" fill="#f1f1f1"/><circle cx="36" cy="34" r="16" fill="#555"/><g stroke="#555" stroke-width="6"><path d="M36 14v40M16 34h40M22 20l28 28M50 20L22 48"/></g><circle cx="36" cy="34" r="7" fill="#f1f1f1"/></svg>
</div>
<div class="abs feat-label" style="left:637px">APP</div>

<div class="abs outer" style="left:924px"></div>
<div class="abs inner" style="left:937px">
  <svg width="76" height="76" viewBox="0 0 76 76"><g stroke="#555" stroke-width="3" fill="none"><path d="M38 2v8M14 12l5 6M62 12l-5 6M4 34h8M64 34h8"/><path d="M26 54c0-10-8-12-8-22a20 20 0 0140 0c0 10-8 12-8 22z"/><path d="M34 54V36h8v18"/></g><rect x="26" y="58" width="24" height="5" rx="2" fill="#555"/><rect x="28" y="66" width="20" height="5" rx="2" fill="#555"/></svg>
</div>
<div class="abs feat-label" style="left:904px">NEW PRODUCT<br>INNOVATION</div>

<section class="abs about">
  <h2>About <em>Quillora</em></h2>
  <p>Lorem ipsum dolor sit amet, consectetur adipiscing elit, sed do eiusmod tempor incididunt ut labore et dolore magna aliqua. Ut enim ad minim veniam, quis nostrud exercitation ullamco laboris nisi ut aliquip ex ea commodo consequat. Duis aute irure dolor in reprehenderit in voluptate velit esse cillum dolore eu fugiat nulla pariatur. Excepteur sint occaecat cupidatat non proident, sunt in culpa qui officia deserunt mollit anim id est laborum.</p>
</section>

<nav class="abs footnav">
  <a class="active" href="#">HOME</a><span class="star">★</span>
  <a href="#">ABOUT US</a><span class="star">★</span>
  <a href="#">SERVICES</a><span class="star">★</span>
  <a href="#">BLOG</a>
</nav>

<div class="abs contactbar">
  <div class="item" style="left:86px"><svg width="20" height="28" viewBox="0 0 20 28"><path d="M10 0a10 10 0 0110 10c0 7-10 18-10 18S0 17 0 10A10 10 0 0110 0z" fill="#ddd"/><circle cx="10" cy="10" r="4" fill="#3a3a3a"/></svg><span style="margin-left:6px">Lorem ipsum dolor sit amet, adipiscing elit</span></div>
  <div class="item" style="left:428px;font-size:17px"><svg width="16" height="24" viewBox="0 0 16 24"><path d="M4 1l4 2-2 6c0 3 1 7 3 9l4-1 2 4-4 3C4 20 0 10 2 2z" fill="#ddd"/></svg><span>+1 555 0134 207</span></div>
  <div class="item" style="left:630px"><span style="font-size:30px;color:#ddd;font-weight:700">@</span><span>info@quillora.com</span></div>
  <div class="item" style="left:836px"><div style="width:40px;height:40px;border-radius:50%;background:#ddd;display:flex;align-items:center;justify-content:center"><svg width="22" height="16" viewBox="0 0 22 16"><rect x="1" y="1" width="20" height="14" rx="2" fill="#3a3a3a"/><path d="M2 3l9 6 9-6" fill="none" stroke="#ddd" stroke-width="1.5"/></svg></div></div>
  <div class="abs email-in">Enter Email</div>
  <div class="abs go">GO</div>
</div>

<footer class="abs bottom">
  <div class="copy">All contents © 2016&nbsp; Quillora. All rights reserved.</div>
  <div class="social-foot" aria-label="Social links">
    <span></span><span></span><span></span><span></span>
  </div>
</footer>
</body>
</html>
```